New Website Deisgn. Guaranteed Project.

I would like a site similar to this: http://givewheelsheal.org.

old site: http://autosforrelief.org

Create a professional website; a car donation site seeking leads to return calls.

Please see http://givewheelsheal.org for the concept I am after.

The webpage should have a professional feel. The pages to include are 'Home', 'About us' and 'Get Started'

Industry/Entity Type

It Professional

Coding

Coded - Design and coding required

Number of Pages Required

1 page

```html
<!DOCTYPE html>
<html lang="en">
<head>
<meta charset="utf-8">
<title>Bright Futures Kids Fund – Donate Your Car</title>
<link href="https://fonts.googleapis.com/css2?family=Open+Sans:wght@400;600;700&display=swap" rel="stylesheet">
<style>
:root{
  --purple:#5a2d6d;
  --purple-dark:#46204f;
  --orange:#f36c21;
  --blue:#2f86d2;
  --yellow:#fdd91b;
  --gold:#e0b13a;
  --ink:#333333;
  --muted:#777777;
  --line:#e3e3e3;
  --black:#050505;
  --white:#ffffff;
}
*{box-sizing:border-box;margin:0;padding:0}
html,body{width:1200px;height:3416px;overflow:hidden;background:var(--white);font-family:"Open Sans",Arial,sans-serif;color:var(--ink)}
.page{position:relative;width:1200px;height:3416px}
.abs{position:absolute}

/* header */
.site-header{left:0;top:0;width:1200px;height:68px;background:var(--purple)}
.brand{left:148px;top:0;width:212px;height:68px;background:var(--white);display:flex;align-items:center;gap:10px;padding-left:14px}
.brand-mark{width:26px;height:26px;border-radius:50%;background:var(--purple)}
.brand-name{font-size:17px;font-weight:600;color:var(--purple);line-height:1.05;width:150px}
.main-nav{right:155px;top:0;height:68px;display:flex;align-items:center;gap:26px}
.main-nav a{color:var(--white);font-size:12px;font-weight:700;text-decoration:none;letter-spacing:.3px}

/* hero */
.hero{left:0;top:68px;width:1200px;height:581px;background:linear-gradient(180deg,#e9e6dc 0%,#cfd3b5 38%,#8fb34a 62%,#5d8f22 100%)}
.hero-title{left:0;top:250px;width:1200px;text-align:center;color:var(--orange);font-size:54px;font-weight:400;line-height:58px}
.hero-sub{left:0;top:375px;width:1200px;text-align:center;color:var(--white);font-size:19px}
.btn-ghost{top:416px;height:40px;border:2px solid var(--white);color:var(--white);font-size:15px;display:flex;align-items:center;justify-content:center;letter-spacing:.5px}
.scroll-down{left:583px;top:597px;width:32px;height:32px}

/* donation form area */
.collage{left:0;top:660px;width:724px;height:463px;background:linear-gradient(120deg,#d8cfc6 0%,#f3f0ec 45%,#f4d7b8 75%,#e9e9e9 100%)}
.form-panel{left:724px;top:660px;width:476px;height:463px;background:#f1f1f1}
.donate-form{left:810px;top:724px;width:354px;height:335px;background:var(--yellow);border-radius:6px;padding:16px 38px}
.donate-form h2{font-size:18px;font-weight:700;text-align:center;color:#222;border-bottom:1px solid #8a7a20;padding-bottom:6px}
.donate-form p{font-size:10px;text-align:center;margin-top:6px;color:#333}
.field-row{display:flex;gap:14px;margin-top:14px}
.field{flex:1;height:26px;background:var(--white);border:1px solid #cfcfcf;font-size:10px;color:#9a9a9a;display:flex;align-items:center;padding-left:8px;justify-content:space-between;padding-right:6px}
.submit{margin:22px auto 0;width:182px;height:30px;border-radius:15px;background:#111;color:var(--white);font-size:10px;font-weight:700;display:flex;align-items:center;justify-content:center}

/* about */
.about-photo{left:0;top:1123px;width:592px;height:489px;background:radial-gradient(ellipse at 40% 45%,#bdbdbd 0%,#d9d9d9 45%,#ffffff 85%)}
.about-copy{left:626px;top:1212px;width:433px}
.about-copy h2{color:var(--blue);font-size:25px;font-weight:400;margin-bottom:8px}
.about-copy p{font-size:11.5px;line-height:17px;color:#555;margin-bottom:14px}

/* features */
.feature{width:274px;border-left:1px solid var(--line);border-right:1px solid var(--line);text-align:center}
.feature .icon{width:82px;height:82px;border-radius:50%;background:#efefef;margin:0 auto;display:flex;align-items:center;justify-content:center}
.feature h3{font-size:13px;font-weight:700;color:var(--purple);margin-top:26px;line-height:16px}

/* why donate */
.why{left:143px;top:2163px;width:500px}
.why h2,.today h2{color:var(--blue);font-size:25px;font-weight:400}
.why ul{list-style:none;margin-top:18px}
.why li{display:flex;gap:16px;height:80px}
.tick{flex:0 0 22px;height:22px;border-radius:50%;background:var(--blue);display:flex;align-items:center;justify-content:center}
.why h4{font-size:13px;font-weight:400;color:#333}
.why span{display:block;font-size:10.5px;color:#666;margin-top:4px;line-height:15px}
.today{left:694px;top:2163px;width:380px}
.today ul{list-style:none;margin-top:10px;font-size:11.5px;line-height:16px;color:#555}
.kid-photo{left:663px;top:2357px;width:355px;height:353px;background:linear-gradient(160deg,#e7a9c8 0%,#d7b7a4 40%,#c5c6cc 75%,#9ea4ad 100%)}

/* get started */
.car-band{left:0;top:2823px;width:1200px;height:140px}
.get-started{left:0;top:2960px;width:1200px;height:410px;background:var(--black)}
.gs-title{left:0;top:3024px;width:1200px;text-align:center;color:var(--gold);font-size:22px;font-weight:400;letter-spacing:.5px}
.step{width:330px;text-align:center}
.step svg{display:block;margin:0 auto}
.step h3{color:var(--gold);font-size:20px;font-weight:400;margin-top:38px}
.step p{color:var(--gold);font-size:13px;line-height:18px;margin-top:2px}

/* footer */
.site-footer{left:0;top:3370px;width:1200px;height:46px;background:var(--purple-dark)}
.social{right:140px;top:3380px;display:flex;gap:22px}
.social span{width:24px;height:24px;border-radius:50%;background:#cbb9d3}
</style>
</head>
<body>
<div class="page">

  <header class="site-header abs">
    <div class="brand abs"><span class="brand-mark"></span><span class="brand-name">Bright Futures Kids Fund</span></div>
    <nav class="main-nav abs">
      <a href="#home">HOME</a><a href="#about">ABOUT</a><a href="#why">WHY DONATE</a><a href="#start">GET STARTED</a>
      <svg width="14" height="14" viewBox="0 0 14 14"><circle cx="6" cy="6" r="4.5" fill="none" stroke="#fff" stroke-width="1.6"/><line x1="9.3" y1="9.3" x2="13" y2="13" stroke="#fff" stroke-width="1.6"/></svg>
    </nav>
  </header>

  <section class="hero abs" id="home" role="img" aria-label="Photo of two young children running happily across a sunny grass field"></section>
  <h1 class="hero-title abs">Donate Your Car to Fight<br>Children's Cancer</h1>
  <p class="hero-sub abs">Your car can make a difference!</p>
  <div class="btn-ghost abs" style="left:471px;width:140px">DONATE CAR</div>
  <div class="btn-ghost abs" style="left:642px;width:69px">CALL US</div>
  <svg class="scroll-down abs" viewBox="0 0 32 32"><circle cx="16" cy="16" r="14" fill="none" stroke="#fff" stroke-width="2"/><polyline points="10,13 16,19 22,13" fill="none" stroke="#fff" stroke-width="2.5"/></svg>

  <div class="collage abs" role="img" aria-label="Collage of a mother and daughter on a sofa, a white compact van and a smiling boy peeking around a wall"></div>
  <div class="form-panel abs"></div>
  <form class="donate-form abs">
    <h2>Fill out the form below</h2>
    <p>to instantly donate online</p>
    <div class="field-row" style="margin-top:20px"><div class="field">First Name</div><div class="field">Last Name</div></div>
    <div class="field-row"><div class="field">Phone</div><div class="field">Email</div></div>
    <div class="field-row"><div class="field">Choose Year <span>▾</span></div><div class="field">Choose Maker <span>▾</span></div></div>
    <div class="field-row"><div class="field">Vehicle Model</div><div class="field">Zip code</div></div>
    <div class="submit">CLICK TO DONATE YOUR CAR</div>
  </form>

  <div class="about-photo abs" id="about" role="img" aria-label="Black and white portrait of a smiling child undergoing cancer treatment"></div>
  <div class="about-copy abs">
    <h2>ABOUT</h2>
    <p>We turn donated vehicles into care for children fighting cancer. Every car, truck or van helps fund treatment, family support and research across the country.</p>
    <p>Donating is simple, fast and free. We handle towing and paperwork for you.</p>
    <p>Your gift is tax deductible, and our team keeps you informed at every step.</p>
    <p>Proceeds support hospital programs, comfort kits and research grants that give young patients and their families real hope during treatment.</p>
    <p>Join thousands of donors who have already helped. Start today with the short form above.</p>
  </div>

  <div class="feature abs" style="left:143px;top:1678px;height:160px">
    <div class="icon"><svg width="34" height="34" viewBox="0 0 34 34" stroke="#5a2d6d" stroke-width="2" fill="none"><line x1="9" y1="4" x2="9" y2="30"/><line x1="17" y1="4" x2="17" y2="30"/><line x1="25" y1="4" x2="25" y2="30"/><rect x="6" y="18" width="6" height="4" fill="#fff"/><rect x="14" y="9" width="6" height="4" fill="#fff"/><rect x="22" y="14" width="6" height="4" fill="#fff"/></svg></div>
    <h3>Car Donations are EASY</h3></div>
  <div class="feature abs" style="left:464px;top:1678px;height:160px">
    <div class="icon"><svg width="34" height="34" viewBox="0 0 34 34" stroke="#5a2d6d" stroke-width="2" fill="none"><circle cx="23" cy="11" r="6"/><line x1="18" y1="16" x2="6" y2="28"/><line x1="9" y1="25" x2="12" y2="28"/></svg></div>
    <h3>Free Pick Up Nationwide</h3></div>
  <div class="feature abs" style="left:786px;top:1678px;height:160px">
    <div class="icon"><svg width="34" height="34" viewBox="0 0 34 34" stroke="#5a2d6d" stroke-width="2" fill="none"><circle cx="17" cy="17" r="12"/><polyline points="11,13 17,19 23,13"/><polyline points="11,18 17,24 23,18"/></svg></div>
    <h3>Tax Deductible</h3></div>
  <div class="feature abs" style="left:143px;top:1881px;height:175px">
    <div class="icon"><svg width="34" height="34" viewBox="0 0 34 34" stroke="#5a2d6d" stroke-width="2" fill="none"><rect x="8" y="5" width="18" height="24"/><line x1="12" y1="11" x2="22" y2="11"/><line x1="12" y1="16" x2="22" y2="16"/><line x1="12" y1="21" x2="22" y2="21"/></svg></div>
    <h3>No Paperwork Hassle</h3></div>
  <div class="feature abs" style="left:464px;top:1881px;height:175px">
    <div class="icon"><svg width="34" height="34" viewBox="0 0 34 34" stroke="#5a2d6d" stroke-width="2" fill="none"><path d="M8 12h6a3 3 0 1 1 6 0h6v14H8z"/><path d="M8 20h4"/></svg></div>
    <h3>Avoid the Hassle of Trying to Sell a Used Car</h3></div>
  <div class="feature abs" style="left:786px;top:1881px;height:175px">
    <div class="icon"><svg width="34" height="34" viewBox="0 0 34 34" stroke="#5a2d6d" stroke-width="2" fill="none"><rect x="6" y="13" width="22" height="6"/><rect x="8" y="19" width="18" height="10"/><line x1="17" y1="13" x2="17" y2="29"/><path d="M17 13c-3-6-9-4-6 0M17 13c3-6 9-4 6 0"/></svg></div>
    <h3>Save Money on Car Bills</h3></div>

  <section class="why abs" id="why">
    <h2>Why Donate Your Car to Us?</h2>
    <ul>
      <li><span class="tick"><svg width="12" height="10" viewBox="0 0 12 10"><polyline points="1,5 4.5,8.5 11,1" fill="none" stroke="#fff" stroke-width="2"/></svg></span><div><h4>IRS 501(c)3 Approved</h4><span>Free 24/7 Pickup with No DMV Hassles.</span></div></li>
      <li><span class="tick"><svg width="12" height="10" viewBox="0 0 12 10"><polyline points="1,5 4.5,8.5 11,1" fill="none" stroke="#fff" stroke-width="2"/></svg></span><div><h4>Free Local Towing to You</h4><span>We will pick up your car donation, running or not, when it's most convenient, at home or work.</span></div></li>
      <li><span class="tick"><svg width="12" height="10" viewBox="0 0 12 10"><polyline points="1,5 4.5,8.5 11,1" fill="none" stroke="#fff" stroke-width="2"/></svg></span><div><h4>IRS 501(c)3 Approved</h4><span>Free 24/7 Pickup with No DMV Hassles.</span></div></li>
      <li><span class="tick"><svg width="12" height="10" viewBox="0 0 12 10"><polyline points="1,5 4.5,8.5 11,1" fill="none" stroke="#fff" stroke-width="2"/></svg></span><div><h4>Income Tax Deduction</h4><span>We issue you an IRS tax receipt &amp; offer the largest resale network to get you the highest tax write-off possible.</span></div></li>
      <li><span class="tick"><svg width="12" height="10" viewBox="0 0 12 10"><polyline points="1,5 4.5,8.5 11,1" fill="none" stroke="#fff" stroke-width="2"/></svg></span><div><h4>No Paperwork Hassles</h4><span>We take any car and handle everything: DMV, Smog and IRS paperwork.</span></div></li>
      <li><span class="tick"><svg width="12" height="10" viewBox="0 0 12 10"><polyline points="1,5 4.5,8.5 11,1" fill="none" stroke="#fff" stroke-width="2"/></svg></span><div><h4>Car donations help fund charitable programs</h4><span>And benefit <b style="color:var(--blue)">Bright Futures Kids Fund</b>, an IRS registered 501(c)3 nonprofit organization.</span></div></li>
      <li><span class="tick"><svg width="12" height="10" viewBox="0 0 12 10"><polyline points="1,5 4.5,8.5 11,1" fill="none" stroke="#fff" stroke-width="2"/></svg></span><div><h4>Schedule a Free Pickup</h4><span>Complete the form and a representative will call you to arrange a convenient time to pickup your car.</span></div></li>
    </ul>
  </section>
  <section class="today abs">
    <h2>Donate Your Car Today!</h2>
    <ul>
      <li>- You have no costs.</li>
      <li>- Free towing, running or not.</li>
      <li>- We issue you an IRS tax receipt.</li>
      <li>- We take care of all paperwork.</li>
      <li>- And we take care of DMV &amp; Smog issues.</li>
    </ul>
  </section>
  <div class="kid-photo abs" role="img" aria-label="Portrait of a smiling girl wearing a pink patterned headscarf"></div>

  <svg class="car-band abs" viewBox="0 0 1200 140" role="img" aria-label="Row of black car silhouettes above the get started band">
    <path d="M0 0 C30 40 60 100 150 140 L0 140Z" fill="#050505"/>
    <path d="M1200 0 C1170 40 1140 100 1050 140 L1200 140Z" fill="#050505"/>
    <rect x="120" y="70" width="960" height="70" fill="#050505"/>
    <rect x="540" y="30" width="120" height="50" rx="14" fill="#050505"/>
  </svg>

  <section class="get-started abs" id="start"></section>
  <h2 class="gs-title abs">GET STARTED</h2>
  <div class="step abs" style="left:47px;top:3100px">
    <svg width="96" height="90" viewBox="0 0 96 90"><polygon points="24,3 72,3 94,45 72,87 24,87 2,45" fill="none" stroke="#e0b13a" stroke-width="2.5"/><rect x="34" y="30" width="26" height="30" fill="none" stroke="#e0b13a" stroke-width="2.5"/><line x1="44" y1="50" x2="64" y2="28" stroke="#e0b13a" stroke-width="3"/></svg>
    <h3>TELL US</h3><p>Fill out our online form or call us at<br>1-800-555-0142</p></div>
  <div class="step abs" style="left:435px;top:3100px">
    <svg width="96" height="90" viewBox="0 0 96 90"><polygon points="24,3 72,3 94,45 72,87 24,87 2,45" fill="none" stroke="#e0b13a" stroke-width="2.5"/><rect x="30" y="42" width="36" height="14" fill="#e0b13a"/><circle cx="38" cy="60" r="5" fill="#e0b13a"/><circle cx="58" cy="60" r="5" fill="#e0b13a"/><line x1="48" y1="42" x2="60" y2="26" stroke="#e0b13a" stroke-width="3"/></svg>
    <h3>WE TOW IT</h3><p>We will arrange a convenient time to<br>collect your vehicle at <b>NO</b> cost to you.</p></div>
  <div class="step abs" style="left:841px;top:3100px">
    <svg width="96" height="90" viewBox="0 0 96 90"><polygon points="24,3 72,3 94,45 72,87 24,87 2,45" fill="none" stroke="#e0b13a" stroke-width="2.5"/><path d="M48 24 L64 30 V46 C64 56 56 62 48 66 C40 62 32 56 32 46 V30Z" fill="#e0b13a"/><circle cx="48" cy="45" r="7" fill="#050505"/></svg>
    <h3>TAX WRITE-OFF</h3><p>We will provide you with a receipt that<br>can be used to declare a tax deduction.</p></div>

  <footer class="site-footer abs"></footer>
  <div class="social abs"><span></span><span></span><span></span><span></span></div>
</div>
</body>
</html>
```